Northfield Energy Product Distribution Brochure

We are looking to have our current brochure for our customers completely redesigned...the idea is to present the relevant information in an attractive way . Our website is northfieldenergy-example.com where you can find more information about us. We have included a file with a rough idea of the page order and what each should include but feel free to adapt based on design. The example provided is only for context and doesnt have to be maintained. We will be using the brochure both digitally and in print form. As long as it reads easily and is eye catching, the design can be horizontal or vertical.Final deliverable should be indesign file.

"Our Brands" page: should be limited to one page (space being enough) where it has the header for each one (for example diesel generators) space for one or two lines of text and then the corresponding logos for each of the five categories
Updates

For those asking: the "our brands" page should be a single page layout where there is a header with the corresponding section and space for maybe one line of text followed by the two logos for that category. Each of the product pages should be similar in fashion to the one in the document attached: a photo of the product with some white space and space for the text to be included. We will be posting additional examples today

Target Market(s)

We want to present it to customers both digitally and in print so they can see our products

Industry/Entity Type

Power Generation

Font styles to use
Serif

Requirements
Must have
• Eye catching and able to present the information in a presentable fashion. Rest is up to you.
Nice to have
• Should incorporate the colors of our logo but can also add other depending on design

```html
<!DOCTYPE html>
<html lang="en">
<head>
<meta charset="utf-8">
<title>Northfield Energy – Product Distribution Brochure</title>
<link href="https://fonts.googleapis.com/css2?family=Montserrat:wght@400;600;700;800&family=Open+Sans:wght@400;600&display=swap" rel="stylesheet">
<style>
  :root{
    --yellow:#f2b51c;
    --yellow-soft:#f7cf5e;
    --charcoal:#353535;
    --slate:#5c5c5c;
    --mist:#ececec;
    --paper:#ffffff;
    --text:#555555;
    --stage:#636363;
  }
  *{margin:0;padding:0;box-sizing:border-box}
  html,body{width:1200px;height:2472px;overflow:hidden}
  body{background:var(--stage);font-family:"Open Sans",Arial,sans-serif;color:var(--text);position:relative}
  .page{position:absolute;background:var(--paper);overflow:hidden;width:540px;height:700px}
  .spread{position:absolute;left:60px;width:1080px;height:700px;box-shadow:0 12px 30px rgba(0,0,0,.35)}
  .spread .page{top:0}
  .spread .page.left{left:0}
  .spread .page.right{left:540px;box-shadow:inset 14px 0 18px -14px rgba(0,0,0,.25)}
  .shapes{position:absolute;inset:0;width:100%;height:100%}
  .photo{position:absolute}
  .heading{font-family:"Montserrat",Arial,sans-serif;font-weight:800;text-transform:uppercase;line-height:1}
  .sub{font-family:"Montserrat",Arial,sans-serif;font-weight:700;text-transform:uppercase}
  .footer{position:absolute;bottom:18px;font-size:8px;line-height:14px;color:var(--slate);font-family:"Montserrat",Arial,sans-serif;font-weight:600;display:flex;align-items:center}
  .footer .pn{display:inline-block;width:14px;height:14px;background:var(--yellow);color:#fff;text-align:center;line-height:14px;margin-right:6px}

  /* cover */
  .cover{left:330px;top:80px;box-shadow:0 12px 30px rgba(0,0,0,.35)}
  .brand{position:absolute;display:flex;align-items:center;gap:8px;font-family:"Montserrat",Arial,sans-serif;font-weight:700;font-size:13px;color:var(--charcoal);letter-spacing:.5px}
  .brand .mark{width:16px;height:16px;background:var(--yellow)}
  .cover .brand{left:300px;top:50px}
  .cover-title{position:absolute;left:300px;top:96px;width:200px}
  .cover-title .heading{font-size:22px;color:var(--yellow)}
  .cover-title .line2{color:var(--charcoal);font-size:16px;margin-top:4px}
  .cover-title p{font-size:9px;margin-top:10px;line-height:1.5}

  /* index */
  .index{position:absolute;left:40px;top:250px;width:290px}
  .index .heading{font-size:40px;color:var(--yellow);margin-bottom:16px}
  .index-list{list-style:none}
  .index-list li{display:flex;align-items:center;justify-content:space-between;border-bottom:1px solid #d8d8d8;padding:5px 0;font-size:12px;line-height:16px;font-family:"Montserrat",Arial,sans-serif;font-weight:600;color:var(--charcoal)}
  .index-list li span.em{color:var(--yellow)}
  .index-list .num{width:18px;height:18px;border-radius:50%;background:var(--yellow);color:#fff;font-size:9px;display:flex;align-items:center;justify-content:center}

  /* about */
  .about-head{position:absolute;left:300px;top:120px;width:210px}
  .about-head .kicker{font-size:10px;color:var(--slate)}
  .about-head .heading{font-size:20px;color:var(--yellow);margin:2px 0 10px}
  .about-head p{font-size:8.5px;line-height:1.55}
  .divider{position:absolute;left:40px;right:40px;top:405px;border-top:1px dashed #c9c9c9}
  .facts{position:absolute;left:40px;top:425px;width:460px;display:grid;grid-template-columns:1fr 1fr;gap:22px 30px}
  .fact h3{font-family:"Montserrat",Arial,sans-serif;font-size:9.5px;font-weight:700;color:var(--yellow);text-transform:uppercase;line-height:1.3;margin-bottom:5px}
  .fact p{font-size:8.5px;line-height:1.5}

  /* stock */
  .stock-grid{position:absolute;left:30px;top:60px;width:300px;display:grid;grid-template-columns:1fr 1fr;gap:22px 18px}
  .product-card .pimg{height:96px;border:1px solid #e4e4e4}
  .product-card h4{font-family:"Montserrat",Arial,sans-serif;font-size:9px;color:var(--charcoal);margin-top:6px;text-transform:uppercase}
  .product-card p{font-size:8px;line-height:1.4}
  .product-card .bar{height:3px;width:34px;background:var(--yellow);margin-top:5px}
  .stock-title{position:absolute;left:375px;top:150px;color:#fff}
  .stock-title .kicker{font-size:16px;font-weight:600;font-family:"Montserrat",Arial,sans-serif}
  .stock-title .heading{font-size:34px;color:var(--yellow)}

  /* transfer switches */
  .switch-title{position:absolute;left:300px;top:215px;width:210px}
  .switch-title .heading{font-size:26px;color:var(--yellow)}
  .switch-title p{font-size:8.5px;line-height:1.55;margin-top:10px}
  .switch-row{position:absolute;left:40px;top:510px;width:460px;display:grid;grid-template-columns:repeat(3,1fr);gap:20px}
  .switch-item .pimg{height:92px;border:1px solid #e4e4e4}
  .switch-item h4{font-family:"Montserrat",Arial,sans-serif;font-size:9px;color:var(--charcoal);margin-top:7px;text-transform:uppercase}
  .switch-item p{font-size:8px;line-height:1.4}
</style>
</head>
<body>

<!-- Cover -->
<section class="page cover" aria-label="Brochure cover">
  <svg class="shapes" viewBox="0 0 540 700" aria-hidden="true">
    <polygon points="0,0 240,0 120,120 0,120" fill="var(--mist)"/>
    <polygon points="150,0 270,0 140,170 60,170" fill="var(--yellow)"/>
    <polygon points="270,0 330,0 200,170 140,170" fill="var(--yellow-soft)"/>
    <polygon points="0,620 540,520 540,700 0,700" fill="var(--mist)"/>
    <polygon points="280,700 540,560 540,600 360,700" fill="var(--yellow)"/>
    <polygon points="380,700 540,610 540,700" fill="var(--charcoal)"/>
  </svg>
  <div class="brand"><span class="mark"></span>NORTHFIELD ENERGY</div>
  <div class="cover-title">
    <div class="heading">Power Solutions</div>
    <div class="heading line2">Product Catalogue</div>
    <p>Generators, parts and switches for every need.</p>
  </div>
  <div class="photo" role="img" aria-label="Photo of a generator control panel in an industrial plant room" style="left:40px;top:210px;width:460px;height:280px;background:linear-gradient(135deg,#4a4a4a,#2b2b2b 60%,#6b5a30)"></div>
  <svg class="shapes" viewBox="0 0 540 700" aria-hidden="true">
    <polygon points="40,490 500,490 500,500 40,500" fill="var(--yellow)"/>
  </svg>
</section>

<!-- Spread: index / about -->
<section class="spread" style="top:876px" aria-label="Index and about spread">
  <div class="page left">
    <svg class="shapes" viewBox="0 0 540 700" aria-hidden="true">
      <polygon points="0,0 220,0 130,110 0,110" fill="var(--mist)"/>
      <polygon points="60,0 200,0 120,90 40,90" fill="var(--yellow)"/>
      <polygon points="200,0 250,0 170,90 120,90" fill="var(--yellow-soft)"/>
    </svg>
    <div class="photo" role="img" aria-label="Photo of three enclosed diesel generators" style="left:300px;top:0;width:240px;height:240px;background:linear-gradient(160deg,#8d8d8d,#3b3b3b)"></div>
    <div class="index">
      <div class="heading">Index</div>
      <ul class="index-list">
        <li><span>About <span class="em">our company</span></span><span class="num">3</span></li>
        <li><span>Our <span class="em">brands</span></span><span class="num">4</span></li>
        <li><span>Our <span class="em">stock</span></span><span class="num">5</span></li>
        <li><span>Standby <span class="em">generators</span></span><span class="num">6</span></li>
        <li><span>Prime <span class="em">generators</span></span><span class="num">7</span></li>
        <li><span>Rental <span class="em">generators</span></span><span class="num">8</span></li>
        <li><span>Air <span class="em">compressors</span></span><span class="num">9</span></li>
        <li><span>Alternator <span class="em">parts</span></span><span class="num">10</span></li>
        <li><span>Light <span class="em">towers</span></span><span class="num">11</span></li>
        <li><span>Transfer <span class="em">switches</span></span><span class="num">12</span></li>
        <li><span>Our <span class="em">distributors</span></span><span class="num">13</span></li>
      </ul>
    </div>
    <div class="footer" style="left:40px"><span class="pn">2</span>NORTHFIELD ENERGY</div>
  </div>
  <div class="page right">
    <div class="photo" role="img" aria-label="Photo of the company operations office" style="left:30px;top:40px;width:240px;height:200px;background:linear-gradient(150deg,#2f3a46,#161b22)"></div>
    <svg class="shapes" viewBox="0 0 540 700" aria-hidden="true">
      <polyline points="20,70 20,30 100,30" fill="none" stroke="var(--yellow)" stroke-width="8"/>
      <polygon points="200,250 280,250 280,180" fill="var(--yellow)"/>
    </svg>
    <div class="about-head">
      <div class="kicker sub">About</div>
      <div class="heading">Our Company</div>
      <p>Northfield Energy supplies dependable power equipment to homes, farms and industry. For over twenty years we have sourced, tested and delivered generators, parts and switches backed by expert service and fast nationwide shipping.</p>
    </div>
    <div class="divider"></div>
    <div class="facts">
      <div class="fact"><h3>Twenty years serving power customers</h3><p>Our team knows the equipment and helps you pick the right unit for the job.</p></div>
      <div class="fact"><h3>Large stock ready to ship</h3><p>Hundreds of units held in our warehouse for quick dispatch across the country.</p></div>
      <div class="fact"><h3>Trusted brands and partners</h3><p>We work only with proven makers so every product meets strict quality standards.</p></div>
      <div class="fact"><h3>Support after the sale</h3><p>Parts, advice and service are available long after your equipment arrives.</p></div>
    </div>
    <div class="footer" style="right:40px">northfieldenergy-example.com <span class="pn" style="margin:0 0 0 6px">3</span></div>
  </div>
</section>

<!-- Spread: stock / transfer switches -->
<section class="spread" style="top:1672px" aria-label="Stock and transfer switches spread">
  <div class="page left">
    <svg class="shapes" viewBox="0 0 540 700" aria-hidden="true">
      <polygon points="540,0 540,700 350,700 350,110" fill="var(--charcoal)"/>
      <polygon points="350,110 540,0 540,40 350,150" fill="var(--yellow)"/>
      <polygon points="430,0 540,0 540,60" fill="var(--mist)"/>
    </svg>
    <div class="stock-grid">
      <div class="product-card"><div class="pimg" role="img" aria-label="Photo of a 20 kW diesel generator" style="background:linear-gradient(#f4f4f4,#cfd3da)"></div><h4>20 kW Diesel</h4><p>Compact standby unit.</p><div class="bar"></div></div>
      <div class="product-card"><div class="pimg" role="img" aria-label="Photo of a 45 kW diesel generator" style="background:linear-gradient(#f4f4f4,#cfd3da)"></div><h4>45 kW Diesel</h4><p>Quiet enclosed model.</p><div class="bar"></div></div>
      <div class="product-card"><div class="pimg" role="img" aria-label="Photo of a 60 kW diesel generator" style="background:linear-gradient(#f4f4f4,#cfd3da)"></div><h4>60 kW Diesel</h4><p>Prime power rated.</p><div class="bar"></div></div>
      <div class="product-card"><div class="pimg" role="img" aria-label="Photo of a 100 kW diesel generator" style="background:linear-gradient(#f4f4f4,#cfd3da)"></div><h4>100 kW Diesel</h4><p>Heavy duty frame.</p><div class="bar"></div></div>
      <div class="product-card"><div class="pimg" role="img" aria-label="Photo of a 150 kW diesel generator" style="background:linear-gradient(#f4f4f4,#cfd3da)"></div><h4>150 kW Diesel</h4><p>Site ready package.</p><div class="bar"></div></div>
      <div class="product-card"><div class="pimg" role="img" aria-label="Photo of a 200 kW diesel generator" style="background:linear-gradient(#f4f4f4,#cfd3da)"></div><h4>200 kW Diesel</h4><p>Industrial output.</p><div class="bar"></div></div>
    </div>
    <div class="stock-title"><div class="kicker">Our</div><div class="heading">Stock</div></div>
    <div class="footer" style="left:30px"><span class="pn">5</span>NORTHFIELD ENERGY</div>
  </div>
  <div class="page right">
    <div class="photo" role="img" aria-label="Photo of green industrial equipment" style="left:0;top:0;width:540px;height:130px;background:linear-gradient(120deg,#4f6b4a,#2e4030)"></div>
    <svg class="shapes" viewBox="0 0 540 700" aria-hidden="true">
      <polygon points="0,0 200,0 120,130 0,130" fill="var(--paper)"/>
      <polygon points="80,130 540,130 540,100 110,100" fill="var(--yellow)"/>
      <polygon points="0,0 140,0 60,90 0,90" fill="var(--mist)"/>
    </svg>
    <div class="photo" role="img" aria-label="Photo of an automatic transfer switch cabinet" style="left:60px;top:170px;width:200px;height:290px;background:linear-gradient(#f1f1f1,#c9ccd1);border:1px solid #e0e0e0"></div>
    <div class="switch-title">
      <div class="heading">Transfer<br>Switches</div>
      <p>Automatic and manual transfer switches move your load to backup power in seconds. Rated for homes, offices and plants, each unit is tested before it leaves our warehouse.</p>
    </div>
    <div class="switch-row">
      <div class="switch-item"><div class="pimg" role="img" aria-label="Photo of a 100 amp transfer switch" style="background:linear-gradient(#f4f4f4,#cfd3da)"></div><h4>100 Amp ATS</h4><p>Residential service.</p></div>
      <div class="switch-item"><div class="pimg" role="img" aria-label="Photo of a 200 amp transfer switch" style="background:linear-gradient(#f4f4f4,#cfd3da)"></div><h4>200 Amp ATS</h4><p>Light commercial use.</p></div>
      <div class="switch-item"><div class="pimg" role="img" aria-label="Photo of a 400 amp transfer switch" style="background:linear-gradient(#f4f4f4,#cfd3da)"></div><h4>400 Amp ATS</h4><p>Industrial sites.</p></div>
    </div>
    <div class="footer" style="right:40px">northfieldenergy-example.com <span class="pn" style="margin:0 0 0 6px">12</span></div>
  </div>
</section>

</body>
</html>
```